Web Design Project

We need a web design for a new business in Orland Park, IL.
We are a restaurant meal delivery business. We deliver from a variety of restaurants. We gives our customers an alternative to just pizza delivery.

Websites we like:
http://www.brambleporter.example/
https://www.quillfetchgo.example/Default.asp
www.wendlerunner.example/

Our current website is www.tovenbasket.example(not to be used as a guide, i'm looking for an original design)
Updates

Please no pictures of anything associated with Pizza.  We are a restaurant delivery business that gives our customers an alternative to just pizza delivery. 

This is my original logo.  I uploaded the file to the job brief and updated the brief some.

Target Market(s)

Two income households with children.

Industry/Entity Type

Business

Requirements
Must have
• Order Now button,and sliding photographs of food.
Nice to have
• a background other than white(it can be white if it works with the design)
Should not have
• A picture of pizza that cant be changed. It is ok if the photo is apart of sliding photo's, but pizza cant be the main focus of our delivery service.

```html
<!DOCTYPE html>
<html lang="en">
<head>
<meta charset="utf-8">
<title>Toven Basket – Restaurant Delivery</title>
<link rel="stylesheet" href="https://fonts.googleapis.com/css2?family=Bree+Serif&family=Courgette&family=Montserrat:wght@400;500;600&display=swap">
<style>
:root{
  --red:#c8000a;
  --red-dark:#a80008;
  --red-deep:#8f0006;
  --red-bright:#d9000c;
  --sky:#bfe3f7;
  --sky-light:#eaf6fd;
  --paper:#f4f4f4;
  --ink:#4a4a4a;
  --ink-dark:#1d1d1d;
  --heading:#5b5b5b;
  --gold:#f8d893;
  --gold-edge:#e7b35d;
  --gold-ink:#7b5a36;
  --green:#1d8f1f;
  --green-dark:#137015;
  --blue:#1f4fa0;
  --white:#ffffff;
}
*{box-sizing:border-box;margin:0;padding:0}
h1,h2,h3{font-weight:400}
html,body{width:1068px;height:1200px;overflow:hidden;background:var(--paper)}
body{font-family:"Montserrat",sans-serif;color:var(--ink)}
.page{position:absolute;left:0;top:0;width:1000px;height:1124px;transform:scale(1.068);transform-origin:0 0;overflow:hidden;
  background:linear-gradient(90deg,var(--sky) 0,var(--paper) 14%,var(--paper) 86%,var(--sky) 100%)}
.abs{position:absolute}

/* header */
.header{left:0;top:0;width:1000px;height:116px;background:linear-gradient(180deg,#fff 0,var(--sky-light) 55%,var(--sky) 100%)}
.date-tab{left:650px;top:0;width:168px;height:19px;background:#e6e6e6;border-radius:0 0 0 10px;font-size:9px;letter-spacing:.5px;color:#555;text-align:center;line-height:19px}
.login-tab{left:810px;top:0;width:72px;height:19px;background:var(--red);border-radius:0 0 10px 0;color:#fff;font-size:9px;line-height:19px;padding-left:14px}
.brand{left:117px;top:38px;display:flex;align-items:center;gap:8px}
.brand-dot{width:24px;height:24px;border-radius:50%;background:var(--red-dark)}
.brand-name{font-family:"Bree Serif",serif;font-size:24px;color:var(--red-dark)}
.tagline{left:362px;top:38px;font-family:"Courgette",cursive;font-size:16px;line-height:20px;color:#e0363c}
.social{display:flex;gap:9px}
.social span{display:block;border-radius:50%;background:#3b5aa3}
.header-social{left:783px;top:35px}
.header-social span{width:28px;height:28px;box-shadow:0 1px 3px rgba(0,0,0,.35)}
.header-social span:nth-child(2){background:#45a8e0}
.header-social span:nth-child(3){background:#4a4a4a}
.phone{left:713px;top:64px;display:flex;align-items:center;gap:8px;font-size:19px;font-weight:500;color:var(--ink-dark)}
.phone b{color:var(--red);font-weight:500}

/* nav */
.nav{left:0;top:116px;width:1000px;height:42px;background:linear-gradient(180deg,var(--red-bright),var(--red-dark));border-top:2px dashed #f06a6a;border-bottom:3px solid var(--red-deep)}
.nav a{position:absolute;top:8px;font-family:"Bree Serif",serif;font-size:16px;color:#fff;text-decoration:none}

/* slider */
.slider-frame{left:128px;top:174px;width:504px;height:230px;background:#fff;border-radius:30px;box-shadow:0 2px 6px rgba(0,0,0,.25)}
.slide{left:138px;top:181px;width:484px;height:214px;border-radius:22px;background:radial-gradient(ellipse at 50% 55%,#e2b26a 0,#c98a3f 45%,#7b4a24 80%,#4a2c18 100%)}
.slide-arrow{top:268px;width:28px;height:32px;background:#d9d9d9;border:1px solid #bdbdbd;display:flex;align-items:center;justify-content:center}
.dots{left:357px;top:409px;display:flex;gap:5px}
.dots span{width:8px;height:8px;border-radius:50%;background:#ccc}
.dots span:first-child{background:var(--red)}

/* ordering */
.order-box{left:648px;top:174px;width:237px;height:229px;background:var(--gold);border:3px solid var(--gold-edge);border-radius:22px}
.order-title{left:648px;top:190px;width:237px;text-align:center;font-family:"Bree Serif",serif;font-size:19px;color:var(--gold-ink)}
.order-rule{left:665px;top:222px;width:202px;height:1px;background:#d9a75a}
.order-label{left:665px;font-size:12px;color:#4a3a2a}
.order-field{left:665px;width:203px;height:24px;background:#fff;border:1px solid #c9a46a}
.order-or{left:648px;top:276px;width:237px;text-align:center;font-family:"Courgette",cursive;font-size:10px;line-height:12px;color:var(--red)}
.order-btn{left:693px;top:342px;width:146px;height:38px;border-radius:6px;background:linear-gradient(180deg,#fff,#cfcfcf);box-shadow:0 2px 3px rgba(0,0,0,.35);font-family:"Courgette",cursive;font-size:22px;color:#333;text-align:center;line-height:38px}

/* welcome */
.welcome-panel{left:128px;top:455px;width:485px;height:405px;background:#fff;border-radius:6px}
.welcome-ribbon{left:117px;top:434px;width:404px;height:48px;background:linear-gradient(180deg,#f7f7f7,#dedede);clip-path:polygon(0 0,97% 0,100% 50%,97% 100%,0 100%);font-family:"Bree Serif",serif;font-size:26px;color:var(--heading);padding:6px 0 0 16px}
.welcome-text{left:152px;top:497px;width:440px;font-size:10.8px;line-height:14.3px;color:#6a6a6a}
.points{left:150px;top:570px;width:440px;list-style:none}
.points li{position:relative;padding-left:16px;font-size:10.5px;line-height:14px;color:var(--ink-dark);margin-bottom:10px}
.points li::before{content:"»";position:absolute;left:0;top:-2px;font-size:14px}
.details{left:166px;top:650px;width:424px;list-style:none}
.details li{position:relative;padding-left:13px;font-size:10.8px;line-height:14px;color:#6a6a6a;margin-bottom:9px}
.details li::before{content:"";position:absolute;left:0;top:3px;width:6px;height:6px;border:1.5px solid var(--red);border-radius:50%}

/* sidebar */
.side-heading{left:648px;font-family:"Bree Serif",serif;font-size:19px;color:#3a3a3a}
.side-card{left:648px;width:237px;background:#fff;border:2px solid #e2e2e2;border-radius:4px}
.book{left:655px;top:465px;width:222px;height:90px;background:linear-gradient(180deg,var(--green),var(--green-dark))}
.book-art{left:780px;top:465px;width:97px;height:90px;background:linear-gradient(90deg,rgba(29,143,31,0),#1b3b1c)}
.book-title{left:663px;top:466px;font-family:"Courgette",cursive;font-size:26px;color:#fff}
.book-text{left:663px;top:508px;width:120px;font-size:9.5px;line-height:12.5px;color:#fff}
.gift-badge{left:649px;top:606px;width:64px;height:64px;background:var(--red);clip-path:polygon(0 0,100% 0,0 100%);}
.gift-new{left:653px;top:614px;font-family:"Courgette",cursive;font-size:13px;color:#fff;transform:rotate(-45deg)}
.gift-title{left:718px;top:613px;font-size:22px;color:var(--blue)}
.gift-sub{left:718px;top:638px;font-size:11px;font-weight:600;color:#e04a14}
.gift-art{left:722px;top:654px;width:156px;height:60px;border-radius:6px;background:linear-gradient(135deg,#f7c23a,#e8452b 45%,#3aa6d8 100%)}
.gift-brand{left:664px;top:706px;font-family:"Bree Serif",serif;font-size:11px;color:var(--red-dark)}
.gift-note{left:664px;top:724px;font-size:9.5px;line-height:12px;color:#333}
.gift-strip{left:760px;top:727px;width:123px;height:31px;background:var(--red-dark);border-radius:40px 0 2px 0;color:#fff;font-size:10.5px;padding:9px 0 0 12px}
.unique{left:655px;top:786px;width:222px;height:66px;background:linear-gradient(180deg,#fff,#dcdcdc)}
.unique-title{left:665px;top:787px;font-family:"Courgette",cursive;font-size:20px;color:var(--red-dark)}
.unique-dot{left:832px;top:797px;width:16px;height:16px;border-radius:50%;background:var(--red-dark)}
.unique-text{left:666px;top:823px;font-size:9.5px;line-height:12.5px;color:#333}
.unique-link{left:803px;top:836px;font-size:10.5px;color:var(--red)}

/* footer */
.footer{left:0;top:884px;width:1000px;height:186px;background:var(--red-dark);border-top:3px dashed #fff}
.footer-bar{left:0;top:1070px;width:1000px;height:38px;background:#9a0007;border-top:1px solid #c52128}
.footer-edge{left:0;top:1108px;width:1000px;height:16px;background:var(--red-bright)}
.foot-heading{font-family:"Bree Serif",serif;font-size:16px;color:#fff}
.map{left:118px;top:936px;width:210px;height:94px;background:linear-gradient(135deg,#e9e4d6,#cfd9c2 60%,#d8d2c0)}
.directions{left:120px;top:1039px;font-size:11px;color:#fff}
.contact-line{left:340px;display:flex;gap:8px;color:#fff}
.divider{left:645px;top:912px;width:1px;height:138px;background:#d94a50}
.quick{top:936px;list-style:none}
.quick li{font-size:10.5px;line-height:19px;color:#fff}
.foot-social{left:119px;top:1076px}
.foot-social span{width:24px;height:24px;background:#fff}
.foot-social span:nth-child(3){background:#444}
.copyright{right:116px;top:1082px;font-size:10px;color:#fff}
</style>
</head>
<body>
<div class="page">

  <header class="abs header"></header>
  <div class="abs date-tab">THURSDAY, JANUARY 03, 2013</div>
  <div class="abs login-tab">LOGIN ⊙</div>
  <div class="abs brand"><span class="brand-dot"></span><span class="brand-name">Toven Basket</span></div>
  <p class="abs tagline">The one stop shop for<br>all your dining needs</p>
  <div class="abs social header-social"><span></span><span></span><span></span></div>
  <div class="abs phone">
    <svg width="32" height="34" viewBox="0 0 32 34"><path d="M6 2c3-1 5 0 6 3l2 5c1 2 0 3-2 4l-2 1c1 4 4 8 8 10l1-2c1-2 3-2 4-1l5 3c2 1 2 3 1 5l-2 2c-3 3-9 1-15-5S2 10 3 5z" fill="#c8000a"/></svg>
    <span><b>(123)</b> 555 0190</span>
  </div>

  <nav class="abs nav">
    <a style="left:117px">Home</a><a style="left:181px">About Us</a><a style="left:265px">Restaurants</a><a style="left:374px">How Do I Order?</a><a style="left:511px">Corporate</a><a style="left:604px">Gift Certificate</a><a style="left:728px">Comments</a><a style="left:826px">Contact</a>
  </nav>

  <div class="abs slider-frame"></div>
  <div class="abs slide" role="img" aria-label="Sliding photo of a freshly baked dish with tomatoes and basil"></div>
  <div class="abs slide-arrow" style="left:123px"><svg width="18" height="10" viewBox="0 0 18 10"><path d="M8 1L2 5l6 4M16 1l-6 4 6 4" stroke="#555" stroke-width="2" fill="none"/></svg></div>
  <div class="abs slide-arrow" style="left:608px"><svg width="18" height="10" viewBox="0 0 18 10"><path d="M2 1l6 4-6 4M10 1l6 4-6 4" stroke="#555" stroke-width="2" fill="none"/></svg></div>
  <div class="abs dots"><span></span><span></span><span></span><span></span></div>

  <div class="abs order-box"></div>
  <div class="abs order-title">ORDERING AREA</div>
  <div class="abs order-rule"></div>
  <div class="abs order-label" style="top:232px">Select Your ZIP Code</div>
  <div class="abs order-field" style="top:251px"><svg class="abs" style="right:0;top:0" width="24" height="22"><rect width="24" height="22" fill="#eee"/><path d="M8 9l4 4 4-4z" fill="#888"/></svg></div>
  <div class="abs order-or">Or</div>
  <div class="abs order-label" style="top:289px">Search For Your ZIP Code</div>
  <div class="abs order-field" style="top:307px"></div>
  <svg class="abs" style="left:664px;top:343px" width="26" height="26" viewBox="0 0 26 26"><path d="M4 2c0 10 6 15 14 15v-5l7 8-7 6v-5C9 21 2 14 4 2z" fill="#2f8a2f"/></svg>
  <div class="abs order-btn">Order now!</div>

  <div class="abs welcome-panel"></div>
  <h1 class="abs welcome-ribbon">Welcome to Toven Basket</h1>
  <p class="abs welcome-text">We really get excited about is delivering culinary delights. Despite the fun name, we take delivery coordination very seriously. As experts in arranging for timely delivery, we coordinate the best food delivery experience for our customers with timely, fresh and professional presentation as our top priorities</p>
  <ul class="abs points">
    <li>Placing an order online or call (555) 4 MEAL NOW (555-463-2566) if you prefer to order by phone.</li>
    <li>Placing an order online or call (555) 4 MEAL NOW (555-463-2566) if you prefer to order by phone.</li>
  </ul>
  <ul class="abs details">
    <li>There is a $15-$50 food minimum per restaurant depending upon delivery location and restaurant.</li>
    <li>There is a delivery fee of $5-$12 for most locations regardless of order size, not including the driver's tip. Gratuity of 15-20% for good service is appreciated.</li>
    <li>Use a credit or debit card online or by phone or pay cash at the door.</li>
    <li>We encourage orders at least two hours in advance in order to guaranty delivery time. This is highly recommended for lunch, large orders, or when ordering from multiple restaurants.</li>
  </ul>

  <h2 class="abs side-heading" style="top:427px">Cotporate</h2>
  <div class="abs side-card" style="top:458px;height:104px"></div>
  <div class="abs book"></div>
  <div class="abs book-art" role="img" aria-label="Photo of a business handshake"></div>
  <div class="abs book-title">Book now</div>
  <p class="abs book-text">It makes checkout easy, &amp; you have the food you want delivered to you.</p>

  <h2 class="abs side-heading" style="top:577px">Gift Certificate</h2>
  <div class="abs side-card" style="top:609px;height:151px"></div>
  <div class="abs gift-badge"></div>
  <div class="abs gift-new">new</div>
  <div class="abs gift-title">Everyone</div>
  <div class="abs gift-sub">Enjoys A Great Meal.</div>
  <div class="abs gift-art" role="img" aria-label="Illustration of wrapped gift boxes"></div>
  <div class="abs gift-brand">Toven Basket</div>
  <p class="abs gift-note">Gift Certificate<br>&nbsp;&nbsp;&nbsp;Available.</p>
  <div class="abs gift-strip">→ Click for more Info</div>

  <div class="abs side-card" style="top:779px;height:81px"></div>
  <div class="abs unique"></div>
  <div class="abs unique-title">Unique Services</div>
  <div class="abs unique-dot"></div>
  <p class="abs unique-text">Now get to stepping with<br>Bramble Porter!</p>
  <div class="abs unique-link">→ Click here</div>

  <footer class="abs footer"></footer>
  <h3 class="abs foot-heading" style="left:117px;top:904px">Contact Us</h3>
  <div class="abs map" role="img" aria-label="Street map of the Marlowe Heights location"></div>
  <div class="abs directions">Get Directions</div>
  <div class="abs contact-line" style="top:935px;font-size:11px;line-height:14px">
    <svg width="12" height="14" viewBox="0 0 12 14"><path d="M6 0a5 5 0 0 1 5 5c0 4-5 9-5 9S1 9 1 5a5 5 0 0 1 5-5z" fill="#f2b8b8"/><circle cx="6" cy="5" r="2" fill="#a80008"/></svg>
    <span style="margin-left:5px">Toven Basket 4820 W Hollis Ave Suite 118<br>Marlowe Heights, NV 89021</span>
  </div>
  <div class="abs contact-line" style="top:971px;font-size:15px">
    <svg width="14" height="12" viewBox="0 0 14 12"><rect x="1" y="1" width="12" height="10" rx="1" fill="none" stroke="#f2b8b8" stroke-width="1.5"/><path d="M3 4h8M3 7h5" stroke="#f2b8b8" stroke-width="1.5"/></svg>
    <span>702-555-0142,&nbsp; 702-555-0187</span>
  </div>
  <div class="abs contact-line" style="top:998px;font-size:12px;color:#ffd23c">
    <svg width="14" height="12" viewBox="0 0 14 12"><path d="M1 5l6-4 6 4v6H1z" fill="none" stroke="#f2b8b8" stroke-width="1.5"/><path d="M1 5l6 4 6-4" fill="none" stroke="#f2b8b8" stroke-width="1.5"/></svg>
    <span>contact@tovenbasket.example</span>
  </div>
  <div class="abs divider"></div>
  <h3 class="abs foot-heading" style="left:696px;top:904px">Quick Links</h3>
  <ul class="abs quick" style="left:696px"><li>Home</li><li>About Us</li><li>Restaurants</li><li>How Do I Order?</li><li>Corporate</li></ul>
  <ul class="abs quick" style="left:812px"><li>Gift Certificate</li><li>Comments</li><li>Contact</li></ul>

  <div class="abs footer-bar"></div>
  <div class="abs social foot-social"><span></span><span></span><span></span></div>
  <div class="abs copyright">Copyright© 2013 Toven Basket. All Rights Reserved.</div>
  <div class="abs footer-edge"></div>

</div>
</body>
</html>
```